Website Development for stormbrookvault.com.au

Build a new Wordpress/Responsive website for stormbrookvault.com.au

Target Market(s)

Compliance Managers, Risk Managers, Information Security and Cyber Security Professionals, Chief Data/Digital Officers, Chief Operating/Financial Officers, Business Continuity Professionals, Disaster Recovery Planners, Small Business Owners, Local/Federal Government entities

Industry/Entity Type

Data Service

Coding

Coded - Design and coding required

Number of Pages Required

5+ page

Font styles to use
Sans Serif

Colors

Designer to choose colors to be used in the design.

Requirements
Must have
• 1. Site Structure: Home Page plus the following chapter-pages for a) Services b) About c) Resources d) Blog e) Contact Us
• 2. Prefer site to built on wordpress and we can purchase a theme if needed (we currently use Kelo4 for other sites)
• 3. Blog needs to be wordpress based
• 4. We will host the site ourselves on our own servers
• 5. Responsive Design
Nice to have
• 1. Livechat capability/interface
• 2. Capability for marketing automation integration (such as pinwhirl, flarevo, quillbranchly etc)
• 3. Capability for CRM integration (Tidewarden)

```html
<!DOCTYPE html>
<html lang="en">
<head>
<meta charset="utf-8">
<title>Stormbrook Vault</title>
<link href="https://fonts.googleapis.com/css2?family=Roboto:wght@400;500;700&family=Mulish:wght@400;600;700&display=swap" rel="stylesheet">
<style>
:root{
  --blue:#1760b8;
  --blue-dark:#0d4a94;
  --navy:#0a1d3f;
  --ink:#222a33;
  --grey:#5b6470;
  --soft:#e8f1fb;
  --line:#d7dde4;
  --white:#ffffff;
  --footer:#17191d;
}
*{box-sizing:border-box;margin:0;padding:0}
html,body{width:1200px;height:4433px;overflow:hidden}
body{position:relative;font-family:"Mulish",sans-serif;color:var(--ink);background:var(--white)}
.abs{position:absolute}
h2{font-family:"Roboto",sans-serif;font-weight:500;font-size:38px;letter-spacing:1px;text-align:center;color:var(--ink)}
.lead{font-size:13px;line-height:20px;color:var(--grey);text-align:center}
.brand{display:flex;align-items:center;gap:8px;font-family:"Mulish",sans-serif;font-weight:700;color:var(--blue)}
.brand .dot{width:26px;height:26px;border-radius:50%;background:var(--blue)}

/* top bar */
.topbar{left:0;top:0;width:1200px;height:44px;display:flex;align-items:center;padding:0 142px;font-size:12px;color:var(--grey);gap:44px}
.topbar .follow{margin-left:auto;display:flex;align-items:center;gap:6px}
.topbar .sq{width:18px;height:18px;background:var(--blue)}
.topbar .sq.r{background:#d34a3a}
.nav-row{left:0;top:44px;width:1200px;height:66px;display:flex;align-items:center;padding:0 142px}
.nav-row .brand{font-size:26px}
.menu{margin-left:auto;display:flex;gap:36px;font-size:12px;font-family:"Roboto",sans-serif;color:var(--ink)}
.menu .on{color:var(--blue);border-bottom:2px solid var(--blue);padding-bottom:6px}

/* hero */
.hero{left:0;top:110px;width:1200px;height:590px;background:linear-gradient(100deg,#061634 0%,#0c2f6a 55%,#0a2250 100%);overflow:hidden}
.hero-art{left:600px;top:20px;width:520px;height:520px;border-radius:50%;background:radial-gradient(circle,#3fd3f0 0%,#1577c2 45%,rgba(10,34,80,0) 72%)}
.hero-text{left:142px;top:132px;color:var(--white)}
.hero-text h1{font-family:"Roboto",sans-serif;font-weight:400;font-size:42px;line-height:58px;letter-spacing:.5px}
.hero-text h1 b{font-weight:700}
.hero-text p{font-size:26px;margin-top:14px;font-family:"Roboto",sans-serif}
.btn-light{display:inline-block;margin-top:34px;background:var(--white);color:var(--blue);font-size:15px;font-weight:600;padding:11px 22px}
.dots{left:560px;top:640px;display:flex;gap:6px}
.dots i{width:18px;height:4px;background:#8fa6c8}
.dots i.on{background:#3fb0ff}

/* about */
.about-photo{left:142px;top:762px;width:448px;height:450px;background:linear-gradient(135deg,#cfd8e2,#7f8fa3)}
.about-photo .brand{position:absolute;left:12px;top:10px;color:var(--white);font-size:16px}
.about-photo .brand .dot{width:14px;height:14px;background:var(--white)}
.about-head{left:632px;top:800px;display:flex;align-items:center;gap:18px}
.about-head span{font-family:"Roboto",sans-serif;font-size:34px;color:var(--grey)}
.about-head .brand{font-size:34px}
.about-head .brand .dot{width:40px;height:40px}
.about-copy{left:630px;top:884px;width:424px;font-size:12.5px;line-height:19px;color:var(--grey)}
.about-copy p{margin-bottom:9px}
.about-copy em{font-style:normal;color:var(--blue)}
.about-copy .cta{color:var(--ink);font-weight:600;font-size:13px}
.about-copy .cta em{font-weight:400}

/* services */
.services{left:0;top:1290px;width:1200px;height:578px;background:var(--soft)}
.services h2{position:absolute;left:0;top:54px;width:1200px}
.services .lead{position:absolute;left:200px;top:124px;width:800px}
.services .lead em{font-style:normal;color:var(--blue)}
.svc{position:absolute;display:flex;align-items:center;gap:18px;font-size:17px;line-height:24px}
.svc.left{flex-direction:row-reverse;text-align:right}
.ring{width:118px;height:118px;border-radius:50%;background:var(--white);border:6px solid #4f5357;display:flex;align-items:center;justify-content:center}
.ring.act{border-color:var(--blue)}
.svc-center{position:absolute;left:496px;top:220px;width:208px;height:270px;display:flex;flex-direction:column;align-items:center;justify-content:center;gap:18px;text-align:center;font-weight:700;font-size:26px;color:var(--blue);line-height:32px}
.svc-center .mark{width:130px;height:130px;border-radius:50%;background:var(--blue)}

/* audience */
.serve h2{position:absolute;left:0;top:1972px;width:1200px}
.serve .lead{position:absolute;left:240px;top:2030px;width:720px}
.aud{position:absolute;top:2098px;width:190px;text-align:center;font-size:16px;line-height:22px;color:var(--grey)}
.aud .circ{width:148px;height:148px;margin:0 auto 20px;border-radius:50%;background:var(--white);box-shadow:0 0 0 8px #eef1f4,0 4px 10px rgba(0,0,0,.12);display:flex;align-items:center;justify-content:center}
.aud.act{color:var(--blue)}
.aud.act .circ{box-shadow:0 0 0 8px var(--blue),0 4px 10px rgba(0,0,0,.12)}
.arrow{position:absolute;width:30px;height:30px;border-radius:50%;background:var(--white);box-shadow:0 1px 4px rgba(0,0,0,.25);display:flex;align-items:center;justify-content:center;font-size:14px;color:var(--grey)}

/* team */
.team{left:0;top:2432px;width:1200px;height:662px;background:linear-gradient(180deg,var(--blue-dark),var(--blue))}
.team h2{position:absolute;left:0;top:84px;width:1200px;color:var(--white)}
.team .sub{position:absolute;left:0;top:136px;width:1200px;text-align:center;color:var(--white);font-size:22px;font-family:"Roboto",sans-serif}
.member{position:absolute;top:192px;width:196px;height:376px;background:var(--white);border-radius:4px;text-align:center}
.member .photo{margin:34px 20px 0;height:206px;background:linear-gradient(160deg,#c9d3de,#6c7a8c);border:1px solid var(--line)}
.member h3{font-family:"Roboto",sans-serif;font-weight:400;font-size:15px;margin-top:20px;letter-spacing:.5px}
.member.act h3{color:var(--blue)}
.member small{display:block;font-size:12px;color:var(--grey);margin-top:4px}
.member .soc{display:flex;justify-content:center;gap:6px;margin-top:10px}
.member .soc i{width:8px;height:8px;background:#9aa3ad}
.member.act{box-shadow:inset 0 0 0 4px #2f7fd8}

/* blog */
.blog{left:0;top:3094px;width:1200px;height:644px;background:linear-gradient(180deg,#f1f6fc,#e1ecf8)}
.blog h2{position:absolute;left:0;top:68px;width:1200px}
.post{position:absolute;top:186px;width:443px;height:281px;background:var(--white);border-radius:6px;border-bottom:5px solid var(--blue);box-shadow:0 2px 8px rgba(0,0,0,.08);text-align:center}
.date{position:absolute;left:166px;top:-58px;width:112px;height:112px;border-radius:50%;background:var(--white);border:8px solid #5f6468;display:flex;flex-direction:column;align-items:center;justify-content:center;color:var(--blue);font-family:"Roboto",sans-serif}
.date b{font-size:38px;font-weight:500;line-height:40px}
.date span{font-size:12px}
.post h3{font-family:"Roboto",sans-serif;font-weight:500;font-size:16px;margin-top:78px}
.post p{font-size:12px;line-height:18px;color:var(--grey);width:340px;margin:14px auto 0}
.post a{display:inline-block;margin-top:14px;color:var(--blue);font-size:12px;text-decoration:underline}
.btn-outline{position:absolute;left:526px;top:520px;width:148px;height:42px;border:2px solid var(--blue);background:var(--white);color:var(--blue);font-size:14px;display:flex;align-items:center;justify-content:center}

/* contact */
.start{left:0;top:3738px;width:1200px;height:560px;background:linear-gradient(180deg,#1a6ac6,#0f57ad)}
.start h2{position:absolute;left:0;top:102px;width:1200px;color:var(--white)}
.form{position:absolute;left:313px;top:186px;width:642px;height:148px;display:grid;grid-template-columns:1fr 1fr;border:1px solid rgba(255,255,255,.35)}
.form .col{display:flex;flex-direction:column}
.field{height:49px;border-bottom:1px solid rgba(255,255,255,.35);border-right:1px solid rgba(255,255,255,.35);padding:16px 16px;color:rgba(255,255,255,.8);font-size:12px}
.field.tall{height:148px;border-right:0}
.submit{position:absolute;left:526px;top:360px;width:148px;height:38px;background:#c3cad2;color:var(--white);font-size:22px;font-weight:600;display:flex;align-items:center;justify-content:center}

/* footer */
.footer{left:0;top:4196px;width:1200px;height:237px}
.footer .brand{position:absolute;left:142px;top:98px;font-size:30px;color:var(--white)}
.footer .brand .dot{background:var(--white);width:34px;height:34px}
.footer .menu{position:absolute;right:142px;top:132px;color:var(--white)}
.footer .legal{position:absolute;left:142px;top:202px;width:916px;display:flex;justify-content:space-between;font-size:11px;color:#c5c9ce}
.chat{left:1018px;top:4226px;width:44px;height:44px;border-radius:50%;background:var(--white);display:flex;align-items:center;justify-content:center}
</style>
</head>
<body>

<header>
  <div class="abs topbar">
    <span>☎ +(03) 555 0142</span>
    <span>✉ info@stormbrookvault.com.au</span>
    <span class="follow">Follow Us on <i class="sq r"></i><i class="sq"></i><i class="sq"></i><i class="sq r"></i></span>
  </div>
  <div class="abs nav-row">
    <div class="brand"><span class="dot"></span>Stormbrook Vault</div>
    <nav class="menu"><span class="on">HOME</span><span>ABOUT</span><span>SERVICES</span><span>RESOURCES</span><span>BLOG</span><span>CONTACT US</span></nav>
  </div>
</header>

<section class="abs hero">
  <div class="abs hero-art" role="img" aria-label="Hands holding a glowing digital globe of technology icons"></div>
  <div class="abs hero-text">
    <h1>DELIVERING <b>QUALITY</b><br>SERVICES THROUGH<br><b>INNOVATION</b></h1>
    <p>From Industry Experts</p>
    <span class="btn-light">Contact Us Today</span>
  </div>
  <div class="abs dots"><i></i><i class="on"></i><i></i></div>
  <svg class="abs" style="left:0;top:440px" width="1200" height="150" viewBox="0 0 1200 150"><path d="M0 40 Q600 230 1200 0 L1200 150 L0 150Z" fill="#fff"/></svg>
</section>

<section class="about">
  <div class="abs about-photo" role="img" aria-label="Businessman working on a laptop at his desk">
    <div class="brand"><span class="dot"></span>Stormbrook Vault</div>
  </div>
  <div class="abs about-head"><span>About</span><div class="brand"><span class="dot"></span>Stormbrook Vault</div></div>
  <div class="abs about-copy">
    <p><em>Stormbrook Vault</em> It is a long established fact that a reader will be distracted by the readable content of a page when looking at its layout. The point of using Lorem Ipsum is that it has a more-or-less normal distribution</p>
    <p>The point of using Lorem Ipsum is that it has a more-or-less normal distribution of letters, as opposed to using 'Content here, content here', making it look like readable English</p>
    <p>Lorem Ipsum is that it has a more-or-less normal distribution of letters, as opposed to using 'Content here, content here', making it look like readable English has a more-or-less normal</p>
    <p>The point of using Lorem Ipsum is that it has a more-or-less normal distribution of letters, as opposed to using 'Content here, content here', making it look like readable English</p>
    <p class="cta">Get the support you need now. <em>Contact our 24/7 support line to get started.</em></p>
  </div>
</section>

<section class="abs services">
  <h2>SERVICES</h2>
  <p class="lead"><em>Stormbrook Vault</em> It is a long established fact that a reader will be distracted by the readable content of a page when looking at its layout.<br>The point of using Lorem Ipsum is that it has a more-or-less normal distribution of letters</p>
  <div class="svc left" style="right:740px;top:218px;color:var(--blue)">
    <div class="ring act"><svg width="50" height="50" viewBox="0 0 50 50" fill="none" stroke="#222" stroke-width="2"><path d="M12 30a9 9 0 0 1 3-17 11 11 0 0 1 21 3 7 7 0 0 1 0 14z"/><path d="M25 30v10M20 40h10"/></svg></div>
    <span>Data Management<br>Platforms</span>
  </div>
  <div class="svc left" style="right:740px;top:372px">
    <div class="ring"><svg width="50" height="50" viewBox="0 0 50 50" fill="none" stroke="#222" stroke-width="2"><ellipse cx="25" cy="12" rx="12" ry="5"/><path d="M13 12v24c0 3 5 5 12 5s12-2 12-5V12M13 24c0 3 5 5 12 5s12-2 12-5"/></svg></div>
    <span>Data Management<br>Services</span>
  </div>
  <div class="svc-center"><span class="mark"></span><span>Stormbrook<br>Vault</span></div>
  <div class="svc" style="left:738px;top:218px">
    <div class="ring"><svg width="50" height="50" viewBox="0 0 50 50" fill="none" stroke="#222" stroke-width="2"><circle cx="20" cy="28" r="8"/><circle cx="34" cy="16" r="6"/><path d="M20 16v4M20 36v4M8 28h4M28 28h4M34 6v4M34 22v4"/></svg></div>
    <span>Industry<br>Solutions</span>
  </div>
  <div class="svc" style="left:738px;top:372px">
    <div class="ring"><svg width="50" height="50" viewBox="0 0 50 50" fill="none" stroke="#222" stroke-width="2"><rect x="10" y="10" width="30" height="30" rx="3"/><path d="M25 16l7 3v6c0 5-3 8-7 9-4-1-7-4-7-9v-6z"/></svg></div>
    <span>Ransomware<br>Protection</span>
  </div>
</section>

<section class="serve">
  <h2>TO WHOM WE SERVE</h2>
  <p class="lead">The point of using Lorem Ipsum is that it has a more-or-less normal distribution of letters, as opposed to using 'Content here, content here', making it look like readable English</p>
  <div class="arrow" style="left:80px;top:2157px">‹</div>
  <div class="aud" style="left:118px"><div class="circ"><svg width="60" height="60" viewBox="0 0 60 60" fill="none" stroke="#333" stroke-width="2"><path d="M30 10 52 48H8z"/><path d="M30 24v12M30 41v2"/></svg></div>Risk Managers</div>
  <div class="aud" style="left:310px"><div class="circ"><svg width="60" height="60" viewBox="0 0 60 60" fill="none" stroke="#333" stroke-width="2"><path d="M30 8l18 7v13c0 12-8 20-18 24-10-4-18-12-18-24V15z"/><path d="M22 30l6 6 11-12"/></svg></div>Information<br>Security</div>
  <div class="aud act" style="left:502px"><div class="circ"><svg width="60" height="60" viewBox="0 0 60 60" fill="none" stroke="#1760b8" stroke-width="2"><rect x="14" y="14" width="32" height="32" rx="3"/><rect x="24" y="28" width="12" height="10"/><path d="M26 28v-4a4 4 0 0 1 8 0v4M20 8v6M30 8v6M40 8v6M20 46v6M30 46v6M40 46v6"/></svg></div>Cyber Security<br>Professionals</div>
  <div class="aud" style="left:694px"><div class="circ"><svg width="60" height="60" viewBox="0 0 60 60" fill="none" stroke="#333" stroke-width="2"><circle cx="30" cy="18" r="7"/><path d="M12 44h36M16 44V32h28v12M24 52h12"/></svg></div>Chief Data<br>Technicians</div>
  <div class="aud" style="left:889px"><div class="circ"><svg width="60" height="60" viewBox="0 0 60 60" fill="none" stroke="#333" stroke-width="2"><circle cx="30" cy="20" r="9"/><path d="M14 50c0-10 7-16 16-16s16 6 16 16z"/></svg></div>Digital Officers</div>
  <div class="arrow" style="left:1090px;top:2157px">›</div>
</section>

<section class="abs team">
  <h2>OUR TEAM</h2>
  <p class="sub">Our Bestest Team Members.</p>
  <div class="arrow" style="left:140px;top:346px">‹</div>
  <div class="member" style="left:192px"><div class="photo" role="img" aria-label="Portrait of team member"></div><h3>MARLOW</h3><small>Designation Here</small><div class="soc"><i></i><i></i><i></i><i></i></div></div>
  <div class="member act" style="left:400px"><div class="photo" role="img" aria-label="Portrait of team member"></div><h3>TESSA VANE</h3><small>Designation Here</small><div class="soc"><i></i><i></i><i></i><i></i></div></div>
  <div class="member" style="left:609px"><div class="photo" role="img" aria-label="Portrait of team member"></div><h3>OWEN FAIRLEY</h3><small>Designation Here</small><div class="soc"><i></i><i></i><i></i><i></i></div></div>
  <div class="member" style="left:816px"><div class="photo" role="img" aria-label="Portrait of team member"></div><h3>REID CALLOWAY</h3><small>Designation Here</small><div class="soc"><i></i><i></i><i></i><i></i></div></div>
  <div class="arrow" style="left:1025px;top:346px">›</div>
</section>

<section class="abs blog">
  <h2>LATEST BLOG POSTS</h2>
  <div class="arrow" style="left:84px;top:320px">‹</div>
  <article class="post" style="left:142px">
    <div class="date"><b>12</b><span>Feb 2019</span></div>
    <h3>The point of using Lorem Ipsum</h3>
    <p>"The point of using Lorem Ipsum is that it has a more-or-less normal distribution of letters, as opposed to using 'Content here, content here', making it look like readable English letters, as opposed to using 'Content here, content here.</p>
    <a>Learn More</a>
  </article>
  <article class="post" style="left:615px">
    <div class="date"><b>06</b><span>Feb 2019</span></div>
    <h3>The point of using Lorem Ipsum</h3>
    <p>"The point of using Lorem Ipsum is that it has a more-or-less normal distribution of letters, as opposed to using 'Content here, content here', making it look like readable English letters, as opposed to using 'Content here, content here.</p>
    <a>Learn More</a>
  </article>
  <div class="arrow" style="left:1086px;top:320px">›</div>
  <div class="btn-outline">View All</div>
</section>

<section class="abs start" role="img" aria-label="Blue-tinted photo of a team meeting around a table">
  <h2>LET'S GET STARTED</h2>
  <div class="form">
    <div class="col"><div class="field">Your Name</div><div class="field">Your Email</div><div class="field" style="border-bottom:0">Your Contact Number</div></div>
    <div class="col"><div class="field tall">Your Message</div></div>
  </div>
  <div class="submit">Submit</div>
</section>

<footer class="abs footer">
  <svg class="abs" style="left:0;top:0" width="1200" height="237" viewBox="0 0 1200 237"><path d="M0 60 Q600 -30 1200 60 L1200 237 L0 237Z" fill="#17191d"/></svg>
  <div class="brand"><span class="dot"></span>Stormbrook Vault</div>
  <nav class="menu"><span>HOME</span><span>ABOUT</span><span>SERVICES</span><span>RESOURCES</span><span>BLOG</span><span>CONTACT US</span></nav>
  <div class="legal"><span>Copyright 2019 @ Stormbrook Vault. All Rights Reserved.</span><span>Terms of services | Privacy Policy</span></div>
</footer>
<div class="abs chat"><svg width="24" height="24" viewBox="0 0 24 24"><path d="M3 5h18v11H9l-5 4v-4H3z" fill="#1760b8"/></svg></div>

</body>
</html>
```